Web Design Project: Facility Management company

Hi! We need a new website.

Our current website: http://www.vireo-trade.ru/ and we don-t like it. =)
The structure of our company has changed and now we don't need "cleaning" and "engeneering" on this site.

We are facility management company in Russia. So we provide integrated service solutions specific to industrial services: maintenance, repair, etc. of facility management.
More services:
Energy planning
Automation
Audit
Statements with regulators
Video surveillance
Central heating
Security systems
Welding
Management of subcontractors
Electrical installation and service needs
Reception
Catering

Visitors:
* Managers in the field of commercial real estate
* Chief engineers
* TOP managers of large companies, malls, factories...
+ their subordinates
* Small% of applicants.

Here you can see some websites/patterns we liked:
http://www.kobalmire.ru/ (This is our competitor’s site, so our site shouldn’t be an exact copy))))
http://www.dwatqo.ru/
http://www.layoutfarrow.com/demo/24296.html
http://www.layoutfarrow.com/website-templates/10145.html

Style:
Light, hi-tech/minimalizm, the color palette should be based on the original site colors (Green + black + white). http://www.vireo-trade.ru/

Estimated sitemap:
1. Home
2. About Us
3. Company's policy
4. History + Achievements.
5. Certificates
6. Map of presence (Here you can use sample map in file "our projects")
7. Services
8. Portfolio
9. News or blog
10. Jobs
11. Contacts - with the feedback form (or the function "call to order")
12. English

Need a design pages: main page, page 404. The rest of the page could be created by general pattern.

Logo, navigation bar and contacts should be visible on all pages of a site.
Flash animation elements and buttons, etc. - not needed.

* We need to develop 3 websites, so we are looking for a long term cooperation.
Looking forward to your creativity =)

Must Have:
Clear, intuitive structure of web pages.
In the center - of pictures reflecting our main services (industrial theme). May be in rotation.
BUT! This banner (central picture) should not be a huge one =)
All relevant information should be visible at once without scrolling.

A possibility to place media files (presentations, video ...) and 2 banner links on the main page.

Font should be available in Cyrillic.
Updates

IMPORTANT!

Please notice that in thisdesign we don't need "cleaning" and "engeneering" on this site.

So don't use old block of 4pictures from our current website. We don't need it anymore. 

Thestructure of our company has changed and now we need some links (may be banners,may be something else) to our future cleaning website as well as engeneeringwebsite.
It should look like seperate (partner) companies, not like our sevices.

Regards, Vera.

Please don't forget that we need bilingual site.

So define language changing tool in your designs.

Industry/Entity Type

Industrial

```html
<!DOCTYPE html>
<html lang="en">
<head>
<meta charset="utf-8">
<title>Vireo Service — Facility Management</title>
<link href="https://fonts.googleapis.com/css2?family=PT+Sans:wght@400;700&family=PT+Sans+Narrow:wght@700&family=Michroma&display=swap" rel="stylesheet">
<style>
:root{
  --green:#a3c139;
  --green-dark:#8eab2c;
  --ink:#111;
  --bar:#1c1c1c;
  --text:#555;
  --muted:#777;
  --line:#d6d6d6;
  --paper:#fff;
}
*{margin:0;padding:0;box-sizing:border-box}
html,body{width:1028px;height:1200px;overflow:hidden;background:var(--paper)}
body{font-family:"PT Sans",Arial,sans-serif;color:var(--text)}
.page{position:relative;width:1028px;height:1200px;overflow:hidden}
.abs{position:absolute}

/* top bar */
.topbar{left:0;top:0;width:1028px;height:40px;background:linear-gradient(#2c2c2c,#222);border-bottom:1px solid #444}
.lang{left:115px;top:14px;font-size:10px;color:#aaa;display:flex;align-items:center;gap:6px}
.flag{width:17px;height:11px;display:inline-block}
.phone{left:733px;top:6px;display:flex;align-items:center;gap:6px;font-family:"PT Sans Narrow",sans-serif;font-weight:700;font-size:23px;color:#fff;letter-spacing:-.5px}

/* nav */
.nav{left:0;top:40px;width:1028px;height:78px;background:linear-gradient(#262626,#0d0d0d 40%,#111)}
.nav a{position:absolute;font-size:12px;text-transform:uppercase;color:#8a8a8a;text-decoration:none;letter-spacing:.2px}
.nav a.active{color:#fff}
.nav a.active::before{content:"";position:absolute;left:-11px;top:3px;border-left:5px solid #fff;border-top:4px solid transparent;border-bottom:4px solid transparent}
.nav .sep{position:absolute;top:17px;width:1px;height:46px;background:#333}
.nav .rule{position:absolute;top:38px;height:1px;border-top:1px dotted #3a3a3a}

/* brand */
.brand{left:0;top:118px;width:1028px;height:120px;background:linear-gradient(#f6f6f6,#fff)}
.brand-name{left:0;width:1028px;top:36px;display:flex;justify-content:center;align-items:center;gap:10px}
.brand-mark{width:14px;height:14px;background:var(--green)}
.brand-word{font-family:"PT Sans",sans-serif;font-weight:400;font-size:26px;color:var(--ink);line-height:1}
.brand-tag{left:0;width:1028px;top:72px;text-align:center;font-size:10px;color:#555}

/* hero */
.hero-band{left:0;top:238px;width:1028px;height:281px;background:var(--green)}
.hero{left:113px;top:238px;width:801px;height:281px;background:#fff}
.hero-photo{left:116px;top:238px;width:795px;height:281px;background:linear-gradient(170deg,#d2d2d2 0%,#9d9d9d 45%,#3e3e3e 80%,#1a1a1a 100%)}
.cap{background:#1a1a1a;color:#fff;white-space:nowrap;padding:0 10px;line-height:1}
.cap b{font-weight:400;color:var(--green)}
.cap-1{left:443px;top:320px;height:30px;font-size:24px;padding-top:3px;letter-spacing:-.5px}
.cap-2{left:600px;top:361px;height:27px;font-size:18px;padding-top:4px;letter-spacing:-.5px}

/* intro */
.intro{left:0;top:519px;width:1028px;height:278px;background:linear-gradient(#f8f8f8,#e6e6e6)}
.h-green{font-size:19px;font-weight:700;color:var(--green);text-transform:uppercase}
.lead{font-size:10px;color:var(--muted)}
.services-list{list-style:none}
.services-list li{position:relative;padding-left:18px;font-size:9.5px;color:var(--muted);height:17.5px;line-height:13px}
.services-list li::before{content:"";position:absolute;left:0;top:3px;width:0;height:0;border-bottom:6px solid var(--green);border-left:11px solid transparent}
.divider-v{width:1px;border-left:1px dotted #bbb}
.welcome{font-family:"Michroma",sans-serif;font-size:24px;color:var(--ink);letter-spacing:-1px}
.icon-ring{width:28px;height:28px;border:3px solid var(--green);border-radius:50%}
.body-copy{font-size:9.8px;line-height:15.7px;color:var(--muted);letter-spacing:.15px}
.btn{height:19px;padding:0 15px 0 8px;border:1px solid #ddd;background:linear-gradient(#f4f4f4,#e6e6e6);font-size:9.5px;font-weight:700;color:#555;line-height:17px;white-space:nowrap}
.btn::before{content:"› "}

/* partners */
.partner{height:82px;border:1px solid #ccc;background:linear-gradient(90deg,#e4e4e4,#9a9a9a 50%,#3a3a3a)}
.partner-cap{background:rgba(20,20,20,.88);color:#fff;text-align:right;padding:7px 10px 0 0;line-height:1}
.partner-cap .l1{font-size:22px;letter-spacing:-.6px}
.partner-cap .l1 b{font-weight:700;font-size:27px}
.partner-cap .l2{font-size:17px;color:var(--green);font-weight:700;margin-top:1px}

/* lower */
.h-dark{font-size:19px;font-weight:700;color:var(--ink);text-transform:uppercase;letter-spacing:.2px}
.news-item{left:119px;width:218px;height:55px}
.date{position:absolute;left:0;top:0;width:34px;height:33px;background:#1e1e1e;color:#fff;text-align:center;line-height:1}
.date .d{font-size:14px;font-weight:700;padding-top:4px;display:block}
.date .m{font-size:8.5px;color:#aaa}
.date::after{content:"";position:absolute;left:11px;bottom:-6px;border-top:6px solid #1e1e1e;border-left:6px solid transparent;border-right:6px solid transparent}
.news-title{position:absolute;left:41px;top:2px;font-size:10px;font-weight:700;color:var(--green);letter-spacing:.3px}
.news-text{position:absolute;left:41px;top:16px;font-size:9.5px;color:var(--muted)}
.news-rule{position:absolute;left:0;top:45px;width:218px;border-top:1px dotted #ccc}
.video{left:378px;top:951px;width:280px;height:177px;background:#111;padding:4px}
.video-inner{width:100%;height:100%;border:2px solid #777;background:linear-gradient(135deg,#e8e8e8,#9a9a9a 55%,#4a4a4a)}
.play{left:480px;top:998px;width:80px;height:80px;border-radius:50%;background:radial-gradient(circle at 40% 35%,#fafafa,#c4c4c4);box-shadow:0 0 0 4px rgba(255,255,255,.5)}
.contact{font-size:9.8px;line-height:14.5px;color:#222}
.contact .k{color:var(--green)}

/* footer */
.footer{left:0;top:1150px;width:1028px;height:50px;background:linear-gradient(#2a2a2a,#050505 40%,#000)}
.copy{left:119px;top:1167px;font-size:9.5px;color:#888}
</style>
</head>
<body>
<div class="page">

  <header>
    <div class="abs topbar"></div>
    <div class="abs lang">Select Your Language:
      <svg class="flag" viewBox="0 0 17 11" aria-label="English"><rect width="17" height="11" fill="#1f3a8a"/><path d="M0 0L17 11M17 0L0 11" stroke="#fff" stroke-width="2.4"/><path d="M0 0L17 11M17 0L0 11" stroke="#c8102e" stroke-width="1"/><path d="M8.5 0V11M0 5.5H17" stroke="#fff" stroke-width="3.6"/><path d="M8.5 0V11M0 5.5H17" stroke="#c8102e" stroke-width="2"/></svg>
      <svg class="flag" viewBox="0 0 17 11" aria-label="Русский"><rect width="17" height="3.67" fill="#fff"/><rect y="3.67" width="17" height="3.67" fill="#1f4fb5"/><rect y="7.33" width="17" height="3.67" fill="#d52b1e"/></svg>
    </div>
    <div class="abs phone">
      <svg width="22" height="22" viewBox="0 0 24 24" aria-hidden="true"><path d="M6.6 10.8a15.1 15.1 0 006.6 6.6l2.2-2.2a1 1 0 011-.25 11.4 11.4 0 003.6.57 1 1 0 011 1V20a1 1 0 01-1 1A17 17 0 013 4a1 1 0 011-1h3.5a1 1 0 011 1c0 1.25.2 2.45.57 3.6a1 1 0 01-.25 1z" fill="#777"/></svg>
      +7 812 400 3182
    </div>

    <nav class="abs nav">
      <a class="active" style="left:170px;top:19px">Home</a>
      <a style="left:170px;top:46px">About us</a>
      <span class="rule" style="left:160px;width:95px"></span>
      <span class="sep" style="left:260px"></span>
      <a style="left:297px;top:19px">Company's policy</a>
      <a style="left:297px;top:46px">History</a>
      <span class="rule" style="left:295px;width:132px"></span>
      <span class="sep" style="left:442px"></span>
      <a style="left:474px;top:19px">Certificates</a>
      <a style="left:474px;top:46px">Map of presence</a>
      <span class="rule" style="left:472px;width:122px"></span>
      <span class="sep" style="left:606px"></span>
      <a style="left:646px;top:19px">Services</a>
      <a style="left:646px;top:46px">Portfolio</a>
      <span class="rule" style="left:640px;width:90px"></span>
      <span class="sep" style="left:748px"></span>
      <a style="left:789px;top:19px">News/ Blog</a>
      <a style="left:789px;top:46px">Jobs</a>
      <span class="rule" style="left:785px;width:118px"></span>
    </nav>

    <div class="abs brand">
      <div class="abs brand-name"><span class="brand-mark"></span><span class="brand-word">Vireo Service</span></div>
      <div class="abs brand-tag">facility management</div>
    </div>
  </header>

  <section>
    <div class="abs hero-band"></div>
    <div class="abs hero"></div>
    <div class="abs hero-photo" role="img" aria-label="Black and white photo of steel scaffolding and construction cranes against a cloudy sky"></div>
    <div class="abs cap cap-1"><b>Commercial</b> Real Estate Management</div>
    <div class="abs cap cap-2"><b>Integrated</b> Operation of Real Estate</div>
  </section>

  <section>
    <div class="abs intro"></div>
    <h2 class="abs h-green" style="left:118px;top:547px">Our Services</h2>
    <p class="abs lead" style="left:120px;top:584px">Our own team of professionals organize and provide:</p>
    <ul class="abs services-list" style="left:119px;top:606px;width:340px">
      <li>Management of commercial real estate</li>
      <li>Operation of commercial real estate</li>
      <li>Operation of industrial hazardous sites</li>
      <li>Operation and maintenance of plants and factories</li>
      <li>Maintenance of industrial and production equipment</li>
      <li>Maintenance of engineering systems and equipment of any complexity</li>
      <li>Design and installation of engineering systems</li>
      <li>Reconstruction and modernization of systems engineering</li>
    </ul>
    <div class="abs btn" style="left:136px;top:753px">read more</div>

    <div class="abs divider-v" style="left:461px;top:548px;height:225px"></div>

    <div class="abs icon-ring" style="left:480px;top:544px"></div>
    <h2 class="abs welcome" style="left:517px;top:540px">WELCOME!</h2>
    <div class="abs body-copy" style="left:481px;top:582px;width:420px">
      <p>We work with you for 8 years. At one time we were one of the first who decided to develop an integrated operation of real estate in Russia. Today we employ more than 500 professionals in the business portfolio of the dozens of projects ranging from small to super regional bank branch mall. creating a company, we have set a goal to get priceless knowledge: what our client wants. Now we can say with confidence that, at least, closer to your desires, and we are ready to listen together to build a mutually beneficial business.</p>
      <p style="margin-top:9px">More and more businesses today - the owners and the companies - developers assigning the operation of buildings with all the engineering equipment is outsourced to professional management company.</p>
    </div>
    <div class="abs btn" style="left:480px;top:753px">read more</div>
  </section>

  <section>
    <div class="abs partner" style="left:116px;top:803px;width:347px" role="img" aria-label="Black and white photo of a modern building under construction"></div>
    <div class="abs partner-cap" style="left:193px;top:819px;width:270px;height:56px"><div class="l1">Your <b>IMMAGINATION</b></div><div class="l2">OUR DESIGN</div></div>
    <div class="abs partner" style="left:469px;top:803px;width:443px" role="img" aria-label="Black and white photo of a worker using a floor cleaning machine"></div>
    <div class="abs partner-cap" style="left:642px;top:819px;width:269px;height:56px"><div class="l1">Excellent <b>CLEANING</b></div><div class="l2">SERVICES</div></div>
  </section>

  <section>
    <h2 class="abs h-dark" style="left:118px;top:906px">New &amp; Events</h2>
    <div class="abs news-item" style="top:951px"><div class="date"><span class="d">15</span><span class="m">Apr</span></div><div class="news-title">Lorem ipsum dolor sit amet</div><div class="news-text">consectetuer adipiscing elit, sed diam ....</div><div class="news-rule"></div></div>
    <div class="abs news-item" style="top:1007px"><div class="date"><span class="d">03</span><span class="m">Apr</span></div><div class="news-title">Lorem ipsum dolor sit amet</div><div class="news-text">consectetuer adipiscing elit, sed diam ....</div><div class="news-rule"></div></div>
    <div class="abs news-item" style="top:1062px"><div class="date"><span class="d">01</span><span class="m">Apr</span></div><div class="news-title">Lorem ipsum dolor sit amet</div><div class="news-text">consectetuer adipiscing elit, sed diam ....</div></div>
    <div class="abs btn" style="left:158px;top:1110px">read more</div>

    <div class="abs divider-v" style="left:365px;top:951px;height:180px"></div>

    <h2 class="abs h-dark" style="left:386px;top:906px">Presentations</h2>
    <div class="abs video"><div class="video-inner" role="img" aria-label="Video still of a business presentation in front of a whiteboard"></div></div>
    <div class="abs play"></div>
    <svg class="abs" style="left:509px;top:1026px" width="26" height="24" viewBox="0 0 26 24" aria-label="Play"><path d="M3 1L24 12L3 23Z" fill="#111"/></svg>

    <div class="abs divider-v" style="left:674px;top:951px;height:180px"></div>

    <div class="abs icon-ring" style="left:699px;top:906px"></div>
    <h2 class="abs h-dark" style="left:738px;top:908px">Contact us</h2>
    <div class="abs contact" style="left:699px;top:950px;width:210px">
      <p>Legal address: 187342, Lesnograd,<br>ul. Lipovaya, 14<br>Postal address: 187356, Lesnograd,<br>Ozernaya, 7</p>
      <p style="margin-top:14px"><span class="k">Phone:</span>&nbsp; +7 812 400 31 82<br><span class="k">Fax:</span>&nbsp;&nbsp;&nbsp;&nbsp;&nbsp; +7 812 455 17 64</p>
      <p style="margin-top:14px"><span class="k">E-mail:</span> mail@vireo-trade.ru.</p>
    </div>
    <div class="abs btn" style="left:698px;top:1110px;letter-spacing:.5px">Click Here to View Map</div>
  </section>

  <footer>
    <div class="abs" style="left:119px;top:1147px;width:790px;border-top:1px dotted #ccc"></div>
    <div class="abs footer"></div>
    <p class="abs copy">© Vireoservice 2012. All right reserved.</p>
  </footer>

</div>
</body>
</html>
```